Mesh Banner Design for Business Premises

We require the design of a large mesh banner to be installed across the front fence of our warehouse. The banner should prominently feature our existing Trelborn logo and brand colours (yellow, white, and black) and be designed to be highly visible from the road.

The overall aesthetic should be strong, masculine, and industrial, reflecting the nature of the scaffolding and construction industry. The background should be predominantly black, with our branding incorporated in yellow and white for strong contrast and readability.

The banner should clearly communicate the full scope of services we provide, including:

Scaffold Design
Scaffold Engineering
Scaffold Installation / Erection
Scaffold Dismantling

It should also indicate the types of projects and clients we service, including:

Commercial
Industrial
Residential
Civil

The design should feel bold and professional, with a construction-oriented style that aligns with the scaffolding industry. It should be clean, impactful, and easy to read from a distance, ensuring passing traffic can quickly understand our services.

Where possible, subtle industrial or structural design elements (such as scaffold components, steel textures, or linework) may be incorporated into the background to reinforce the industry theme while keeping the layout uncluttered.

The final design will be produced as a large-format mesh banner for outdoor installation, so it should be created with this application and viewing distance in mind.

```html
<!DOCTYPE html>
<html lang="en">
<head>
<meta charset="utf-8">
<title>Trelborn Mesh Banner</title>
<link rel="stylesheet" href="https://fonts.googleapis.com/css2?family=Oswald:wght@500;600&display=swap">
<style>
  :root {
    --canvas: #e6e6e6;
    --charcoal: #2f2f30;
    --ink: #2b2a28;
    --yellow: #f9b51b;
    --amber: #f7a21a;
    --pale: #fcc94a;
    --white: #ffffff;
  }
  * { margin: 0; padding: 0; box-sizing: border-box; }
  html, body {
    width: 1200px;
    height: 1001px;
    overflow: hidden;
    background: var(--canvas);
  }
  .canvas {
    position: relative;
    width: 1200px;
    height: 1001px;
  }
  .banner {
    position: absolute;
    left: 40px;
    top: 261px;
    width: 1120px;
    height: 479px;
    display: flex;
    overflow: hidden;
  }
  .brand-panel {
    position: relative;
    width: 540px;
    height: 100%;
    background: var(--charcoal);
  }
  .brand-name {
    position: absolute;
    left: 0;
    width: 100%;
    top: 176px;
    text-align: center;
    font-family: "Oswald", sans-serif;
    font-weight: 500;
    font-size: 40px;
    letter-spacing: 0.42em;
    padding-left: 0.42em;
    color: var(--white);
    line-height: 1;
  }
  .brand-name .mark {
    display: inline-block;
    width: 18px;
    height: 18px;
    background: var(--yellow);
    margin-right: 20px;
    vertical-align: middle;
    position: relative;
    top: -4px;
  }
  .phone {
    position: absolute;
    left: 0;
    width: 100%;
    top: 290px;
    text-align: center;
    font-family: "Oswald", sans-serif;
    font-weight: 600;
    font-size: 80px;
    line-height: 1;
    color: var(--yellow);
    letter-spacing: 0.01em;
  }
  .hazard-stripes {
    position: absolute;
    display: block;
  }
  .hazard-stripes.bottom { left: 308px; bottom: 0; }
  .hazard-stripes.top { right: 32px; top: 0; }
  .info-panel {
    position: relative;
    flex: 1;
    height: 100%;
  }
  .site-photo {
    position: absolute;
    inset: 0;
    background: linear-gradient(160deg, var(--amber) 0%, var(--pale) 45%, var(--yellow) 75%, var(--amber) 100%);
  }
  .info-list {
    position: absolute;
    left: 52px;
    list-style: none;
    font-family: "Oswald", sans-serif;
    font-weight: 600;
    font-size: 29px;
    line-height: 36px;
    color: var(--ink);
    text-transform: uppercase;
    letter-spacing: 0.01em;
  }
  .sectors { top: 68px; }
  .services { top: 287px; }
</style>
</head>
<body>
<main class="canvas">
  <section class="banner">
    <div class="brand-panel">
      <div class="brand-name"><span class="mark"></span>TRELBORN</div>
      <div class="phone">1300 5 RAISE</div>
      <svg class="hazard-stripes bottom" width="155" height="74" viewBox="0 0 155 74" aria-hidden="true">
        <polygon points="27,0 56,0 29,74 0,74" fill="var(--white)"/>
        <polygon points="76,0 105,0 78,74 49,74" fill="var(--white)"/>
        <polygon points="126,0 155,0 128,74 99,74" fill="var(--white)"/>
      </svg>
    </div>
    <div class="info-panel">
      <div class="site-photo" role="img" aria-label="Photo of scaffolders working on a steel scaffold frame, tinted yellow"></div>
      <svg class="hazard-stripes top" width="155" height="74" viewBox="0 0 155 74" aria-hidden="true">
        <polygon points="27,0 56,0 29,74 0,74" fill="var(--white)"/>
        <polygon points="76,0 105,0 78,74 49,74" fill="var(--white)"/>
        <polygon points="126,0 155,0 128,74 99,74" fill="var(--white)"/>
      </svg>
      <ul class="info-list sectors">
        <li>Commercial</li>
        <li>Industrial</li>
        <li>Residential</li>
        <li>Civil</li>
      </ul>
      <ul class="info-list services">
        <li>Scaffold Design</li>
        <li>Scaffold Engineering</li>
        <li>Scaffold Installation / Erection</li>
        <li>Scaffold Dismantling</li>
      </ul>
    </div>
  </section>
</main>
</body>
</html>
```